Construction Business Card Design

We have a landscape construction company based in Australia
Were out of business cards ,
So now we're after a fresh looking modern card to give a fresh look to our business ....
We would like the business card to have the
(Front)
Tallow Ridge Pty Ltd
Director Gordon Marsh
0412563908
(Back)
Landscape,Construction,Paving,Excavation
(In smaller font low in the frame of card)
Different textures , curved edge , vertical and horizontal designs also minimal colours per design
Eg one side black , one coloured or a splash here or there
Industry/Entity Type
Landscape
Contact Information for Business Card
Tallow Ridge Pty Ltd
Director Gordon Marsh
0412563908
Landscape,Paving,Construction,Excavation

```html
<!DOCTYPE html>
<html lang="en">
<head>
<meta charset="utf-8">
<title>Tallow Ridge Pty Ltd – Business Card</title>
<link rel="stylesheet" href="https://fonts.googleapis.com/css2?family=EB+Garamond:wght@400&display=swap">
<style>
  :root {
    --card-black: #151314;
    --paper: #ffffff;
    --ink-light: #ebe7e2;
    --accent-teal: #2a7f98;
    --motif-light: #8d8b88;
    --motif-dark: #3d5f69;
    --serif: "EB Garamond", Garamond, "Times New Roman", serif;
  }
  html, body {
    margin: 0;
    padding: 0;
    width: 1200px;
    height: 726px;
    overflow: hidden;
    background: var(--paper);
  }
  .business-card {
    position: relative;
    width: 1200px;
    height: 726px;
    background: var(--card-black);
    border-radius: 67px 0 67px 0;
    overflow: hidden;
    font-family: var(--serif);
    color: var(--ink-light);
  }
  .motif {
    position: absolute;
    background: linear-gradient(135deg, var(--motif-light), var(--motif-dark));
    opacity: 0.55;
  }
  .motif--upper {
    left: 112px;
    top: 112px;
    width: 203px;
    height: 208px;
  }
  .motif--lower {
    left: 884px;
    top: 402px;
    width: 204px;
    height: 206px;
  }
  .director-line {
    position: absolute;
    left: 357px;
    top: 238px;
    margin: 0;
    font-size: 44px;
    font-weight: 400;
    line-height: 1;
    white-space: nowrap;
  }
  .company-name {
    position: absolute;
    left: 0;
    width: 1200px;
    top: 336px;
    margin: 0;
    text-align: center;
    font-size: 44px;
    font-weight: 400;
    line-height: 1;
    letter-spacing: 0.28em;
    text-transform: uppercase;
    color: var(--accent-teal);
    white-space: nowrap;
  }
  .phone {
    position: absolute;
    left: 580px;
    top: 436px;
    margin: 0;
    font-size: 44px;
    font-weight: 400;
    line-height: 1;
    letter-spacing: 0.01em;
    white-space: nowrap;
  }
</style>
</head>
<body>
  <main class="business-card">
    <div class="motif motif--upper" role="img" aria-label="Stepped checker-square motif rising to the upper right"></div>
    <p class="director-line">Director Gordon Marsh</p>
    <h1 class="company-name">Tallow Ridge Pty Ltd</h1>
    <p class="phone">0412563908</p>
    <div class="motif motif--lower" role="img" aria-label="Stepped checker-square motif tapering downward"></div>
  </main>
</body>
</html>
```